Zielgruppe
Wir sind ein Fliesenlegerbetrieb und sind auf der suche nach Mitarbeitern / Fliesenleger. Unsere Kunden sind Privatkunden sowie Öffentliche und Gewerbliche Auftraggeber. Das design soll für Arbeitsuchende ansprechend sein und zu unserem CI passen. Inspiration zu unserem CI finden SIe unter www.fliesen-worlak.de
Aufgabenstellung
Es handelt sich um eine Stellenanzeige die wir im Format 90x50 mm quer und im Format 90 x 90 mm benötigen. In Farbe und S/W.
Unser Textvorschlag, Der Designer darf aucg selbst kreativ sein / werden.
Du arbeitest selbständig und verantwortungsbewusst, hast Freude am Kundenkontakt und kannst jedes Problem lösen ? Dann komm direkt zu uns !
Das erwartet Dich bei uns:
- Junges eingespieltes Team
- Sehr gutes Betriebsklima
- Faire Bezahlung
- Baustellenfahrzeug + Werkzeug
- Unbefristetes Arbeitsverhältnis
- Heimatnahe Baustellen
- Öffentliche, Gewerbliche, Private Baustellen
Kontaktdaden damit sich der Bewerber auch bei uns melden kann !

```html
<!DOCTYPE html>
<html lang="de">
<head>
<meta charset="utf-8">
<title>Stellenanzeige Fliesenleger</title>
<link rel="stylesheet" href="https://fonts.googleapis.com/css2?family=Roboto:ital,wght@0,300;0,400;0,700;0,900;1,700&family=Poppins:wght@400&display=swap">
<style>
  :root {
    --red: #d42027;
    --grey: #8e8e8e;
    --text: #3d3d3d;
    --ink: #1a1a1a;
    --white: #ffffff;
    --photo-light: #efe6dc;
    --photo-warm: #c98d58;
  }
  * { box-sizing: border-box; margin: 0; padding: 0; }
  html, body { width: 1200px; height: 1200px; overflow: hidden; background: var(--white); }
  body { position: relative; font-family: "Roboto", sans-serif; }

  .ad { position: absolute; left: 100px; top: 325px; width: 1007px; height: 557px; background: var(--white); }
  .ad__bar { position: absolute; left: 0; width: 100%; height: 11px; background: var(--grey); }
  .ad__bar--top { top: 0; }
  .ad__bar--bottom { bottom: 0; }

  .brand { position: absolute; left: 48px; top: 62px; font-size: 23px; font-weight: 700; color: var(--ink); letter-spacing: 0.2px; }

  .headline { position: absolute; left: 49px; top: 116px; font-size: 31px; font-weight: 900; line-height: 37px; color: var(--red); letter-spacing: 1.6px; text-transform: uppercase; }

  .intro { position: absolute; left: 49px; top: 196px; width: 560px; font-size: 19px; font-weight: 400; line-height: 25.5px; color: var(--text); letter-spacing: 0.2px; }
  .intro em { font-style: italic; font-weight: 700; color: var(--red); }

  .invite { position: absolute; left: 49px; top: 257px; font-size: 22px; font-weight: 300; color: var(--red); letter-spacing: -0.3px; }

  .benefit { position: absolute; width: 110px; margin-left: -55px; text-align: center; }
  .benefit__icon { display: block; width: 45px; height: 45px; margin: 0 auto; }
  .benefit__label { margin-top: 5px; font-family: "Poppins", sans-serif; font-size: 9px; line-height: 13.5px; color: var(--text); letter-spacing: 0.3px; }

  .contact { position: absolute; left: 309px; top: 426px; width: 277px; height: 81px; background: var(--red); border-radius: 12px; padding: 10px 0 0 38px; color: var(--white); font-size: 14.6px; line-height: 20.6px; }
  .contact__post { position: absolute; top: 507px; width: 15px; height: 39px; background: var(--grey); }

  .photo-frame { position: absolute; left: 662px; top: 51px; width: 300px; height: 455px; background: var(--grey); }
  .photo { position: absolute; left: 18px; top: 18px; width: 264px; height: 418px; border-radius: 9px; background: linear-gradient(160deg, var(--photo-light) 0%, #e6dacd 55%, var(--photo-warm) 100%); }
</style>
</head>
<body>
  <section class="ad">
    <div class="ad__bar ad__bar--top"></div>

    <div class="brand">Fliesen-Worlak</div>

    <h1 class="headline">Stellen für<br>Fliesenleger verfügbar.</h1>

    <p class="intro">Du arbeitest <em>selbständig</em> und <em>verantwortungsbewusst</em>, hast Freude am Kundenkontakt und kannst jedes <em>Problem lösen</em>?</p>

    <p class="invite">Dann komm direkt zu uns !</p>

    <div class="benefit" style="left:94px; top:316px;">
      <svg class="benefit__icon" viewBox="0 0 45 45"><circle cx="22.5" cy="22.5" r="22.5" fill="var(--red)"/><g fill="none" stroke="#fff" stroke-width="2.4"><circle cx="22.5" cy="15.5" r="4"/><circle cx="16" cy="27" r="4"/><circle cx="29" cy="27" r="4"/></g></svg>
      <div class="benefit__label">Junges<br>eingespieltes Team</div>
    </div>
    <div class="benefit" style="left:207px; top:316px;">
      <svg class="benefit__icon" viewBox="0 0 45 45"><circle cx="22.5" cy="22.5" r="22.5" fill="var(--red)"/><rect x="12" y="17" width="21" height="14" rx="2" fill="#fff"/><path d="M18 17v-3h9v3" fill="none" stroke="#fff" stroke-width="2.2"/><path d="M12 23h21" stroke="var(--red)" stroke-width="1.5"/></svg>
      <div class="benefit__label">Sehr<br>gutes Betriebsklima</div>
    </div>
    <div class="benefit" style="left:321px; top:316px;">
      <svg class="benefit__icon" viewBox="0 0 45 45"><circle cx="22.5" cy="22.5" r="22.5" fill="var(--red)"/><text x="25" y="22" font-family="Roboto, sans-serif" font-size="13" font-weight="700" fill="#fff">$</text><path d="M11 27c4-2 8-2 11 0h6c2 0 2 3 0 3h-7m-10 2c4 2 10 3 14 1l8-5" fill="none" stroke="#fff" stroke-width="2.2" stroke-linecap="round" stroke-linejoin="round"/></svg>
      <div class="benefit__label">Faire<br>Bezahlung</div>
    </div>
    <div class="benefit" style="left:435px; top:316px;">
      <svg class="benefit__icon" viewBox="0 0 45 45"><circle cx="22.5" cy="22.5" r="22.5" fill="var(--red)"/><path d="M15 15v6m-3-3h6M14 24v4h17a3 3 0 0 0 0-6h-9" fill="none" stroke="#fff" stroke-width="2.4" stroke-linecap="round"/></svg>
      <div class="benefit__label">Baustellenfahrzeug<br>+ Werkzeug</div>
    </div>
    <div class="benefit" style="left:549px; top:316px;">
      <svg class="benefit__icon" viewBox="0 0 45 45"><circle cx="22.5" cy="22.5" r="22.5" fill="var(--red)"/><rect x="10" y="18" width="22" height="11" rx="1" fill="#fff"/><circle cx="21" cy="23.5" r="2.6" fill="var(--red)"/><rect x="29" y="15" width="7" height="8" rx="1.5" fill="#fff"/><rect x="31" y="18" width="3" height="3" fill="var(--red)"/></svg>
      <div class="benefit__label">Unbefristetes<br>Arbeitsverhältnis</div>
    </div>
    <div class="benefit" style="left:94px; top:421px;">
      <svg class="benefit__icon" viewBox="0 0 45 45"><circle cx="22.5" cy="22.5" r="22.5" fill="var(--red)"/><path d="M21 14v16M13 22h16" stroke="#fff" stroke-width="5"/><path d="M31 11v6M28 14h6" stroke="#fff" stroke-width="1.8"/></svg>
      <div class="benefit__label">Heimatnahe<br>Baustellen</div>
    </div>
    <div class="benefit" style="left:207px; top:421px;">
      <svg class="benefit__icon" viewBox="0 0 45 45"><circle cx="22.5" cy="22.5" r="22.5" fill="var(--red)"/><g fill="#fff"><rect x="19.5" y="12" width="6" height="5"/><rect x="13" y="26" width="5" height="5"/><rect x="20" y="26" width="5" height="5"/><rect x="27" y="26" width="5" height="5"/></g><path d="M22.5 17v9M15.5 26v-4h14v4" fill="none" stroke="#fff" stroke-width="1.8"/></svg>
      <div class="benefit__label">Öffentliche, Gewerbliche,<br>Private Baustellen</div>
    </div>

    <div class="contact">
      Telephone:&nbsp; 0 12 34 / 5 67 89 00<br>
      Mobile: 01 70 / 1 23 45 67<br>
      Email: info@fliesen-worlak.de
    </div>
    <div class="contact__post" style="left:362px;"></div>
    <div class="contact__post" style="left:525px;"></div>

    <div class="photo-frame">
      <div class="photo" role="img" aria-label="Foto: Hände eines Fliesenlegers setzen eine weiße Fliese ins Kleberbett an der Wand"></div>
    </div>

    <div class="ad__bar ad__bar--bottom"></div>
  </section>
</body>
</html>
```